Website for virtual assistant and proofreader

Professional, feminine (but not flowery!) website offering and explaining my services as a VA and Proofreader. Probably only 7 pages: home, about, services (x2), fees, testimonials and contact page. <br/><br/>I already have most of the content, which I have uploaded so you can get an idea of waht I do. I have brand colours and logo already also uploaded. I really just need the bones of the site to be designed and am happy/capable of setting this up as a Wordpress site. I'm just rubbish at design!

Industry/Entity Type

Business Service

Coding

Coded - Design and coding required

Number of Pages Required

4 page

Other font styles liked:
• Roboto Bold + Great Vibes

Colors
3276b5
fee3d4

Requirements
Must have
• should be informative, professional, feminine. Clean, clear, CTA's links to services and fees pages
• Also, see all 3 colour codes on the attached doc.
Nice to have
• business images but place holders will do
Should not have
• Nothing flowery or cartoons! Not 'busy'

```html
<!DOCTYPE html>
<html lang="en">
<head>
<meta charset="utf-8">
<title>Clara M Whitfield – Virtual Assistant and Proofreader</title>
<link href="https://fonts.googleapis.com/css2?family=Roboto:wght@400;500;700&family=Great+Vibes&display=swap" rel="stylesheet">
<style>
:root{
  --blue:#13608f;
  --taupe:#877d7a;
  --ink:#222;
  --text:#333;
  --star:#f39200;
  --navy:#343a4f;
  --footer:#232323;
  --footer-line:#3a3a3a;
  --white:#fff;
}
*{box-sizing:border-box;margin:0;padding:0}
html,body{width:1200px;height:2719px;overflow:hidden}
body{font-family:'Roboto',sans-serif;color:var(--text);background:var(--white);position:relative}
.abs{position:absolute}
a{color:inherit;text-decoration:none}

/* header */
.topbar{top:0;left:0;width:1200px;height:84px}
.contact-chip{top:29px;display:flex;align-items:center;gap:10px}
.chip-icon{width:32px;height:32px;border:1px solid #bbb;border-radius:6px;display:flex;align-items:center;justify-content:center}
.chip-label{font-size:10px;font-weight:700;color:var(--ink)}
.chip-value{font-size:12px;font-weight:500;color:var(--blue)}
.brand{left:510px;top:38px;width:180px;display:flex;align-items:center;justify-content:center;gap:6px}
.brand-dot{width:14px;height:14px;border-radius:50%;background:var(--blue)}
.brand-name{font-size:14px;font-weight:500;color:var(--blue);line-height:1.1}
.nav{top:84px;left:0;width:1200px;height:35px;background:var(--blue);display:flex;justify-content:center;align-items:center}
.nav a{font-size:9px;font-weight:700;color:var(--white);padding:0 19px;position:relative;letter-spacing:.2px}
.nav a+a::before{content:"";position:absolute;left:0;top:2px;height:7px;border-left:1px solid rgba(255,255,255,.4)}
.nav a.active{color:#e9b89a}

/* hero */
.hero{top:119px;left:0;width:1200px;height:430px;background:linear-gradient(100deg,#dfe4ea 0%,#f3f4f6 35%,#e9e9eb 60%,#c9c7c8 100%)}
.hero-script{left:234px;top:121px;font-family:'Great Vibes',cursive;font-size:58px;color:#1f1f1f}
.hero-sub{left:234px;top:187px;font-size:18px;font-weight:700;color:#222}
.btn{display:inline-block;background:var(--blue);color:var(--white);font-size:9.5px;font-weight:700;text-align:center;line-height:31px;height:31px;width:125px}
.hero .btn{position:absolute;left:234px;top:233px}

/* welcome */
.portrait{left:230px;top:619px;width:320px;height:320px;border-radius:50%;border:3px solid #8a8584;background:radial-gradient(circle at 50% 45%,#d7a27e 0%,#a46446 45%,#6b3a24 100%)}
.signature{left:220px;top:940px;width:340px;text-align:center;font-family:'Great Vibes',cursive;font-size:38px;color:var(--blue);white-space:nowrap}
.section-script{font-family:'Great Vibes',cursive;color:var(--blue);font-weight:400}
.welcome-title{left:588px;top:590px;font-size:44px}
.welcome-copy{left:590px;top:650px;width:376px;font-size:9.3px;line-height:11.9px;color:#333}
.welcome-copy p{margin-bottom:12px}
.welcome .btn{position:absolute;left:590px;top:986px}

/* services */
.services{top:1067px;left:0;width:1200px;height:408px;background:var(--taupe)}
.services-title{width:1200px;text-align:center;top:30px;font-size:44px;color:var(--white)}
.services-intro{left:275px;top:92px;width:650px;text-align:center;font-size:9.5px;line-height:16px;color:var(--white);font-weight:500}
.card{top:165px;width:169px;height:199px;background:var(--white);text-align:center;padding-top:19px}
.card-icon{width:55px;height:55px;border-radius:50%;background:var(--blue);margin:0 auto 13px}
.card h3{font-size:11.5px;font-weight:500;color:#222;line-height:19px;padding:0 10px}
.card p{font-size:9.5px;color:#555;line-height:16px;margin-top:6px;padding:0 10px}
.card a{display:block;font-size:8px;font-weight:700;color:var(--blue);text-decoration:underline;margin-top:6px}

/* contact */
.contact-title{width:1200px;text-align:center;top:1505px;font-size:44px}
.form{left:424px;top:1585px;width:349px;height:158px;border:1px solid var(--navy)}
.field{position:absolute;font-family:Georgia,serif;font-style:italic;font-size:9px;color:#333}
.hline{position:absolute;left:0;width:347px;border-top:1px solid var(--navy)}
.vline{position:absolute;left:174px;top:0;height:80px;border-left:1px solid var(--navy)}
.submit{left:656px;top:1743px;width:117px;height:33px;background:var(--navy);color:var(--white);font-family:Georgia,serif;font-size:9.5px;text-align:center;line-height:33px}

/* certifications */
.certs{top:1817px;left:0;width:1200px;height:227px;background:linear-gradient(180deg,#1c6a98,#15618f)}
.certs h2{position:absolute;top:46px;width:1200px;text-align:center;font-size:14.5px;font-weight:500;color:var(--white);letter-spacing:.3px}
.cert-list{position:absolute;top:87px;list-style:none}
.cert-list li{font-size:9.5px;font-weight:500;color:var(--white);height:22.6px;display:flex;align-items:flex-start;gap:6px;white-space:nowrap}

/* testimonials */
.testi-title{width:1200px;text-align:center;top:2078px;font-size:30px}
.tcard{top:2138px;width:232px;height:183px;border:1px solid #e3e3e3;background:var(--white)}
.quote{position:absolute;left:20px;top:16px;font-size:20px;font-weight:700;color:#333;line-height:1}
.stars{position:absolute;right:20px;top:16px;display:flex}
.tcard p{position:absolute;left:21px;top:47px;width:195px;font-size:10px;line-height:15px;color:#666}
.avatar{position:absolute;left:20px;top:117px;width:48px;height:48px;border-radius:50%;background:linear-gradient(135deg,#c9b7a6,#6d7d8c)}
.tname{position:absolute;left:79px;top:127px;font-size:11px;font-weight:500;color:#111}
.trole{position:absolute;left:79px;top:144px;font-size:10px;color:var(--blue)}
.dots{top:2349px;left:564px;display:flex;gap:4px}
.dots span{width:22px;height:2px;background:#999}
.dots span:first-child{background:var(--blue)}

/* footer */
.footer{top:2396px;left:0;width:1200px;height:323px;background:var(--footer)}
.subscribe-input{left:234px;top:32px;width:208px;height:32px;background:#3d3d3d;color:#777;font-size:8px;line-height:32px;padding-left:12px}
.subscribe-btn{left:450px;top:32px;width:95px;height:32px;background:var(--blue);color:var(--white);font-size:8.5px;font-weight:700;text-align:center;line-height:32px}
.social{top:37px;width:22px;height:22px;border-radius:50%;background:#3d3d3d}
.rule{left:234px;width:731px;border-top:1px solid var(--footer-line)}
.f-brand{left:234px;top:130px;font-size:17px;font-weight:500;color:var(--white);display:flex;align-items:center;gap:6px}
.f-brand-dot{width:10px;height:10px;border-radius:50%;background:var(--white)}
.f-tag{left:237px;top:152px;font-size:7.5px;color:#bbb}
.f-info{left:234px;font-size:8.5px;color:#aaa}
.f-info b{font-weight:400;color:var(--white)}
.f-col{top:130px}
.f-col h4{font-size:9.5px;font-weight:700;color:var(--white);margin-bottom:9px}
.f-col li{list-style:none;font-size:8.5px;color:#888;height:17.5px}
.copyright{top:294px;width:1200px;text-align:center;font-size:8px;color:#999}
.copyright b{font-weight:400;color:var(--white)}
</style>
</head>
<body>

<header class="abs topbar">
  <div class="abs contact-chip" style="left:234px">
    <div class="chip-icon"><svg width="14" height="10" viewBox="0 0 14 10"><rect x="0.5" y="0.5" width="13" height="9" fill="#13608f"/><polyline points="1,1 7,6 13,1" fill="none" stroke="#fff" stroke-width="1.2"/></svg></div>
    <div><div class="chip-label">Email Us:</div><div class="chip-value">clara@whitfield.org</div></div>
  </div>
  <div class="abs brand"><span class="brand-dot"></span><span class="brand-name">Clara M Whitfield</span></div>
  <div class="abs contact-chip" style="left:842px">
    <div class="chip-icon"><svg width="14" height="14" viewBox="0 0 24 24"><path fill="#13608f" d="M6.6 10.8a15.1 15.1 0 006.6 6.6l2.2-2.2a1 1 0 011-.25 11.4 11.4 0 003.6.57 1 1 0 011 1V20a1 1 0 01-1 1A17 17 0 013 4a1 1 0 011-1h3.5a1 1 0 011 1c0 1.25.2 2.45.57 3.6a1 1 0 01-.25 1z"/></svg></div>
    <div><div class="chip-label">Call Us:</div><div class="chip-value">+66 80 555 0142</div></div>
  </div>
</header>

<nav class="abs nav">
  <a class="active">HOME</a><a>SERVICES</a><a>SYSTEM APPLICATIONS</a><a>FEES</a><a>WHY ME?</a><a>CONTACT</a>
</nav>

<section class="abs hero" role="img" aria-label="Photo of a hand writing with a pen on paperwork beside a laptop">
  <div class="abs hero-script">Allow me...</div>
  <div class="abs hero-sub">to handle the details so you can get on with business.</div>
  <a class="btn">LEARN MORE</a>
</section>
<svg class="abs" style="top:440px;left:0" width="1200" height="115" viewBox="0 0 1200 115">
  <path d="M0 15 Q600 150 1200 15 L1200 115 L0 115 Z" fill="#877d7a"/>
  <path d="M0 6 Q600 146 1200 6 L1200 115 L0 115 Z" fill="#fff" transform="translate(0,6)"/>
</svg>

<section class="welcome">
  <div class="abs portrait" role="img" aria-label="Portrait photo of the virtual assistant"></div>
  <div class="abs signature">Clara M Whitfield</div>
  <h2 class="abs section-script welcome-title">Welcome</h2>
  <div class="abs welcome-copy">
    <p>Every great leader is backed by diligent and knowledgeable support. Have you ever wondered what it would be like to have your very own personal assistant? Well, you can. A virtual assistant can do everything a full-time assistant can, with the added bonus that she can save you money. Whether you need daily help, or help with special assignments or big projects, hiring me as your VA will save you the costs typically associated with an employee–holiday pay, sick pay, overtime, taxes, and insurance, are no longer your concern. And, as a virtual assistant, I only charge for the hours I actually work–no more resource-siphoning downtime.</p>
    <p>Allow me to be of service. Answering emails, organizing client files, managing projects, updating website content, proofreading content, they are all important tasks but not so important that you have to do them yourself. I have rescued many businesses from the throws of chaos, bringing order to a seemingly endless onslaught of details and procedures. I can make your business function optimally. And as an independent agent, I can do it for a fraction of the cost of a full-time right-hand assistant.</p>
    <p>From organizing existing businesses to creating systems and procedures to launching a fledgling business, I offer decades of experience mastering the minutiae so your business can function at its optimum.</p>
    <p>So trust your important tasks to a professional specially qualified to handle the mundane and minutiae. Delegate to an expert and restore the life-work balance that will benefit you, your clients, and your personal relationships.</p>
    <p>Isn't it time you hire the right-hand support your business needs and you deserve?</p>
  </div>
  <a class="btn">LEARN MORE</a>
</section>

<section class="abs services">
  <h2 class="abs section-script services-title">Our Services</h2>
  <p class="abs services-intro">Do you need some Smart Office Support (SOS)? Do you have a huge project looming on the horizon? Do you just need a little support managing the growing stacks of To-Dos cluttering your desk? As a master of managing the barrage of daily details that require concise and prompt attention, SOS is my speciality, from organisation to proofreading, no detail is too small!</p>
  <div class="abs card" style="left:234px"><div class="card-icon" role="img" aria-label="Project management icon"></div><h3>Organizational/Project Management</h3><p>Reliable project and team management, master of organisation</p><a>Learn More</a></div>
  <div class="abs card" style="left:422px"><div class="card-icon" role="img" aria-label="Accounting icon"></div><h3>Administrative and Accounting Support</h3><p>Work smarter not harder with the right VA by your side</p><a>Learn More</a></div>
  <div class="abs card" style="left:610px"><div class="card-icon" role="img" aria-label="Website icon"></div><h3>Website<br>Administration</h3><p>Dependable and reliable website updates–like clockwork</p><a>Learn More</a></div>
  <div class="abs card" style="left:797px"><div class="card-icon" role="img" aria-label="Proofreading icon"></div><h3>Editorial Service /Proofreading</h3><p>Catching simple typos and grammatical faux pas to preserve your integrity</p><a style="margin-top:0">Learn More</a></div>
</section>

<h2 class="abs section-script contact-title">Contact Us</h2>
<div class="abs form">
  <div class="hline" style="top:40px"></div>
  <div class="hline" style="top:80px"></div>
  <div class="vline"></div>
  <span class="field" style="left:15px;top:15px">First Name</span>
  <span class="field" style="left:189px;top:15px">Last Name</span>
  <span class="field" style="left:15px;top:55px">Email</span>
  <span class="field" style="left:189px;top:55px">Phone</span>
  <span class="field" style="left:15px;top:88px">Type your message here...</span>
</div>
<div class="abs submit">Submit</div>

<section class="abs certs">
  <h2>CERTIFICATIONS AND QUALIFICATIONS</h2>
  <ul class="cert-list" style="left:385px">
    <li><svg width="11" height="9" viewBox="0 0 11 9"><polyline points="1,4.5 4,7.5 10,1" fill="none" stroke="#fff" stroke-width="1.4"/></svg>Professional Certificate for Proofreading</li>
    <li><svg width="11" height="9" viewBox="0 0 11 9"><polyline points="1,4.5 4,7.5 10,1" fill="none" stroke="#fff" stroke-width="1.4"/></svg>Diploma for Word Processing and Spreadsheets</li>
    <li><svg width="11" height="9" viewBox="0 0 11 9"><polyline points="1,4.5 4,7.5 10,1" fill="none" stroke="#fff" stroke-width="1.4"/></svg>Thai language – A1</li>
    <li><svg width="11" height="9" viewBox="0 0 11 9"><polyline points="1,4.5 4,7.5 10,1" fill="none" stroke="#fff" stroke-width="1.4"/></svg>Spanish to GCSE Level – A1</li>
    <li><svg width="11" height="9" viewBox="0 0 11 9"><polyline points="1,4.5 4,7.5 10,1" fill="none" stroke="#fff" stroke-width="1.4"/></svg>Certified Book-keeping Stage 1</li>
  </ul>
  <ul class="cert-list" style="left:611px">
    <li><svg width="11" height="9" viewBox="0 0 11 9"><polyline points="1,4.5 4,7.5 10,1" fill="none" stroke="#fff" stroke-width="1.4"/></svg>Qualified TEFL teacher</li>
    <li><svg width="11" height="9" viewBox="0 0 11 9"><polyline points="1,4.5 4,7.5 10,1" fill="none" stroke="#fff" stroke-width="1.4"/></svg>Trade Guild Certificate in Public House Management</li>
    <li><svg width="11" height="9" viewBox="0 0 11 9"><polyline points="1,4.5 4,7.5 10,1" fill="none" stroke="#fff" stroke-width="1.4"/></svg>6 C.S.E. Grade 3 and above, 2 'O' Levels</li>
    <li><svg width="11" height="9" viewBox="0 0 11 9"><polyline points="1,4.5 4,7.5 10,1" fill="none" stroke="#fff" stroke-width="1.4"/></svg>Many other online courses</li>
  </ul>
</section>

<h2 class="abs section-script testi-title">Testimonials</h2>
<div class="abs tcard" style="left:233px">
  <span class="quote">”</span>
  <div class="stars"><svg width="96" height="11" viewBox="0 0 96 11"><g fill="#f39200"><polygon id="s" points="5.5,0 7,3.9 11,4 7.9,6.5 9,10.5 5.5,8.2 2,10.5 3.1,6.5 0,4 4,3.9"/><use href="#s" x="21"/><use href="#s" x="42"/><use href="#s" x="63"/><use href="#s" x="84"/></g></svg></div>
  <p>Lorem ipsum dolor sit amet, consectetur adipiscing elit. Quisque iaculis elementum eleifend. Cras malesuada vitae enim id imperdiet. Vestibulum vestibulum egestas.</p>
  <div class="avatar" role="img" aria-label="Client photo"></div>
  <div class="tname">DANIEL MORROW</div><div class="trole">Client</div>
</div>
<div class="abs tcard" style="left:483px">
  <span class="quote">”</span>
  <div class="stars"><svg width="96" height="11" viewBox="0 0 96 11"><g fill="#f39200"><use href="#s"/><use href="#s" x="21"/><use href="#s" x="42"/><use href="#s" x="63"/><use href="#s" x="84"/></g></svg></div>
  <p>Lorem ipsum dolor sit amet, consectetur adipiscing elit. Quisque iaculis elementum eleifend. Cras malesuada vitae enim id imperdiet. Vestibulum vestibulum egestas.</p>
  <div class="avatar" role="img" aria-label="Client photo"></div>
  <div class="tname">DANIEL MORROW</div><div class="trole">Client</div>
</div>
<div class="abs tcard" style="left:733px">
  <span class="quote">”</span>
  <div class="stars"><svg width="96" height="11" viewBox="0 0 96 11"><g fill="#f39200"><use href="#s"/><use href="#s" x="21"/><use href="#s" x="42"/><use href="#s" x="63"/><use href="#s" x="84"/></g></svg></div>
  <p>Lorem ipsum dolor sit amet, consectetur adipiscing elit. Quisque iaculis elementum eleifend. Cras malesuada vitae enim id imperdiet. Vestibulum vestibulum egestas.</p>
  <div class="avatar" role="img" aria-label="Client photo"></div>
  <div class="tname">DANIEL MORROW</div><div class="trole">Client</div>
</div>
<div class="abs dots"><span></span><span></span><span></span></div>

<footer class="abs footer">
  <div class="abs subscribe-input">Enter your email...</div>
  <div class="abs subscribe-btn">SUBSCRIBE</div>
  <div class="abs social" style="left:884px"></div>
  <div class="abs social" style="left:913px"></div>
  <div class="abs social" style="left:942px"></div>
  <div class="abs rule" style="top:93px"></div>
  <div class="abs f-brand"><span class="f-brand-dot"></span>Clara M Whitfield</div>
  <div class="abs f-tag">Virtual Assistant and Proofreader</div>
  <div class="abs f-info" style="top:187px">Phone: <b>+66 80 555 0142</b></div>
  <div class="abs f-info" style="top:207px">Email: <b>clara@whitfield.org</b></div>
  <div class="abs f-col" style="left:434px"><h4>SERVICES</h4><ul><li>Organizational/Project Management</li><li>Administrative and Accounting Support</li><li>Website Administration</li><li>Editorial Service/Proofreading</li></ul></div>
  <div class="abs f-col" style="left:654px"><h4>TERM OF USE</h4><ul><li>Terms and Conditions</li><li>Copyright</li><li>Refund Policy</li><li>Privacy Policy</li><li>Disclaimer</li></ul></div>
  <div class="abs f-col" style="left:817px"><h4>MORE LINKS</h4><ul><li>FAQs</li><li>Contact</li><li>Blog</li><li>Work with Us</li></ul></div>
  <div class="abs rule" style="top:264px"></div>
  <div class="abs copyright">Copyright © 2020 <b>Clara M Whitfield</b> All rights reserved.</div>
</footer>

</body>
</html>
```